International IT and cyber security consulting company is looking to establish a web presence.

Harwell Mariner Advisory LLC provides IT, cyber security, risk, project management and data analytics consulting services worldwide. Our clients are both government and corporate. We are looking to establish a basic web presence with about 6 pages (Home, About Harwell, Our Experts, News and Events, Careers, Contact Us). The designs should set the look and feel of the site for further build out down the line. The final design should be straightforward and simple and allow us to convey information about our consulting services clearly.

Target Market(s)

Government and corporate clients or potential clients, job seekers.

Industry/Entity Type

Consulting

Contact Information for Business Card

The cards will have english on the front and arabic on the back. The design should be the same on both sides.

Coding

Number of Pages Required

Font styles to use
Serif
Sans Serif

Requirements
Must have
• The pages should be simple but visually appealing with a picture or graphic that is appropriate to the company or services we offer. Our name and logo should be branded throughout the design. While we are mostly an IT company we also have a line of business where we organize speaking events for VIPs so the website shouldn't overly emphasize our IT work.
Should not have
• No cartoons or drawings. The site should not have overly flashy or loud colors. We cater to a conservative set of clients so the site should match what they expect to see in an international consultancy's website. There should not be an overuse of the color orange because it can be hard on the eyes if it is used too much on the page. Also, please do not use graphics or pictures that use locks, keys, castles, shields etc since these are too commonly used in the cyber security industry.

```html
<!DOCTYPE html>
<html lang="en">
<head>
<meta charset="utf-8">
<title>Harwell Mariner Advisory LLC</title>
<link href="https://fonts.googleapis.com/css2?family=Noto+Serif:wght@400&family=Open+Sans:wght@400&display=swap" rel="stylesheet">
<style>
:root{
  --accent:#d9502a;
  --ink:#1e1e1e;
  --text:#333;
  --disc:#c6c6cb;
  --disc-light:#ececec;
  --band:#f3f3f3;
  --white:#fff;
}
*{margin:0;padding:0;box-sizing:border-box}
html,body{width:1200px;height:3119px;overflow:hidden}
body{position:relative;background:var(--white);font-family:"Open Sans",sans-serif;color:var(--text)}
.abs{position:absolute}
.serif{font-family:"Noto Serif",serif}
.disc{position:absolute;border-radius:50%;background:var(--disc)}
.disc.light{background:var(--disc-light)}
.heading{position:absolute;left:0;width:1200px;text-align:center;font-family:"Noto Serif",serif;color:var(--accent);font-size:34px;font-weight:400;line-height:44px;text-transform:uppercase}

/* header */
.brand{left:144px;top:14px;display:flex;align-items:center;gap:10px}
.brand-name{font-family:"Noto Serif",serif;color:var(--accent);font-size:19px;line-height:22px;text-transform:uppercase;letter-spacing:.5px}
.brand-mark{width:14px;height:14px;border-radius:50%;background:var(--accent)}
.email{right:145px;top:20px;font-family:"Noto Serif",serif;font-size:20px;color:var(--ink);display:flex;align-items:center;gap:10px}
.nav{left:392px;top:70px;display:flex;gap:34px;font-family:"Noto Serif",serif;font-size:13px;color:var(--ink);text-transform:uppercase}
.nav .active{color:var(--accent)}

/* hero */
.hero{left:0;top:100px;width:1200px;height:514px;background:linear-gradient(120deg,#0d1a26 0%,#18374d 45%,#2a6f8c 70%,#0f2232 100%)}
.hero-title{left:144px;top:290px;font-family:"Noto Serif",serif;font-size:33px;line-height:40px;color:var(--white);text-transform:uppercase}
.btn-outline{left:145px;top:378px;width:120px;height:39px;border:1px solid var(--white);color:var(--white);font-family:"Noto Serif",serif;font-size:16px;display:flex;align-items:center;justify-content:center}
.arrow{position:absolute}

/* welcome */
.welcome-text{left:145px;top:780px;width:910px;text-align:center;font-size:13px;line-height:27px;color:var(--text)}

/* services */
.services-photo{left:0;top:963px;width:600px;height:560px;background:linear-gradient(135deg,#2a3c74 0%,#3652b8 50%,#9fb4e8 100%)}
.services-panel{left:600px;top:987px;width:600px;height:560px;background:var(--ink)}
.services-title{left:142px;top:55px;font-family:"Noto Serif",serif;font-size:34px;color:var(--accent);text-transform:uppercase}
.service{position:absolute;left:142px;display:flex;align-items:center;gap:22px;font-family:"Noto Serif",serif;font-size:20px;color:#eee}
.service svg{width:62px;height:58px}

/* news */
.card{position:absolute;top:1674px;width:287px}
.card-img{width:287px;height:191px}
.card-title{margin-top:10px;font-family:"Noto Serif",serif;font-size:16.5px;line-height:22px;color:var(--ink)}
.card-date{margin-top:6px;font-size:11.5px;color:var(--accent)}
.btn-solid{position:absolute;width:112px;height:39px;background:var(--ink);color:var(--white);font-family:"Noto Serif",serif;font-size:16px;display:flex;align-items:center;justify-content:center;text-transform:uppercase}

/* experts */
.experts-band{left:0;top:2096px;width:1200px;height:424px;background:var(--band)}
.expert{position:absolute;top:2232px;width:436px;height:210px}
.expert-photo{position:absolute;left:0;top:0;width:208px;height:208px;border-radius:50%;border:4px solid #2b2b2b;background:linear-gradient(160deg,#d8d4cf,#8f8a85)}
.expert-name{position:absolute;left:219px;top:6px;font-family:"Noto Serif",serif;font-size:26px;color:var(--ink)}
.expert-role{position:absolute;left:219px;top:40px;font-family:"Noto Serif",serif;font-size:14.5px;color:var(--ink)}
.expert-rule{position:absolute;left:219px;top:66px;width:217px;height:3px;background:#2b2b2b}
.expert-bio{position:absolute;left:219px;top:84px;width:217px;font-size:11px;line-height:19px;color:var(--ink)}
.expert-more{position:absolute;left:219px;top:178px;font-family:"Noto Serif",serif;font-size:11.5px;color:var(--ink);text-decoration:underline}

/* contact */
.field{position:absolute;border:1px solid #bdbdbd;background:var(--white);font-size:12px;color:#444;padding:12px 15px}

/* footer */
.footer{left:0;top:3007px;width:1200px;height:112px;background:var(--ink)}
.footer-links{left:144px;top:32px;font-size:12px;color:#cfcfcf;word-spacing:2px}
.footer-copy{left:144px;top:63px;font-size:12px;color:#cfcfcf}
.social{position:absolute;top:48px;width:20px;height:20px;border-radius:50%;border:2px solid #cfcfcf}
</style>
</head>
<body>

<!-- disc behind hero -->
<div class="disc" style="left:18px;top:461px;width:266px;height:266px"></div>

<!-- hero -->
<div class="abs hero" role="img" aria-label="Hooded figure working at glowing computer monitors in a dark server room"></div>
<h1 class="abs hero-title">Phasellus consequat<br>sagittis suscipit feugiat</h1>
<div class="abs btn-outline">READ MORE</div>
<svg class="arrow" style="left:54px;top:342px" width="20" height="30" viewBox="0 0 20 30"><path d="M16 3 L5 15 L16 27" fill="none" stroke="#fff" stroke-width="4"/></svg>
<svg class="arrow" style="left:1124px;top:342px" width="20" height="30" viewBox="0 0 20 30"><path d="M4 3 L15 15 L4 27" fill="none" stroke="#fff" stroke-width="4"/></svg>

<div class="disc light" style="left:29px;top:671px;width:72px;height:72px"></div>

<!-- header -->
<div class="abs brand">
  <div class="brand-name">Harwell<br>Mariner<br>Advisory LLC</div>
  <div class="brand-mark"></div>
</div>
<div class="abs email">
  <svg width="20" height="15" viewBox="0 0 20 15"><rect x="0" y="0" width="20" height="15" rx="2" fill="#1e1e1e"/><path d="M1 2 L10 9 L19 2" fill="none" stroke="#fff" stroke-width="1.6"/></svg>
  info@harwellmarineradvisory.com
</div>
<nav class="abs nav">
  <span class="active">Home</span><span>About Harwell</span><span>Our Experts</span><span>News and Events</span><span>Careers</span><span>Contact Us</span>
</nav>
<div class="disc" style="left:1079px;top:49px;width:97px;height:97px"></div>

<!-- welcome -->
<h2 class="heading" style="top:684px">Welcome to<br>Harwell Mariner Advisory LLC</h2>
<p class="abs welcome-text">Pellentesque a imperdiet dolor, et auctor est. Fusce sollicitudin lorem et luctus volutpat. Proin placerat dapibus gravida. In tristique tristique nulla eget hendrerit. Maecenas vel tortor accumsan quam varius imperdiet vel eget elit. Aenean facilisis tincidunt lectus, id dictum nisi luctus eget. Vivamus efficitur ex condimentum, malesuada eros eget, feugiat nibh. Sed tellus ex, imperdiet eget gravida sit amet, volutpat eget turpis. In nec ultricies est. Etiam mattis augue vehicula odio posuere, sit amet tempus lectus luctus. Etiam vel massa elementum, bibendum tellus venenatis.</p>

<!-- services -->
<div class="abs services-photo" role="img" aria-label="Consultant in glasses writing beside holographic data dashboards"></div>
<section class="abs services-panel">
  <h2 class="abs services-title">What we do</h2>
  <div class="service" style="top:130px">
    <svg viewBox="0 0 62 58" fill="none" stroke="#fff" stroke-width="2"><rect x="6" y="2" width="30" height="20"/><path d="M2 26 H60 M4 26 V56 M44 26 V56 M58 26 V56 M44 36 H58 M44 46 H58 M10 32 H30"/></svg>
    <span>IT Services</span></div>
  <div class="service" style="top:210px">
    <svg viewBox="0 0 62 58" fill="none" stroke="#fff" stroke-width="2"><rect x="4" y="4" width="54" height="38" rx="3"/><path d="M24 42 V50 M38 42 V50 M16 52 H46"/><circle cx="31" cy="23" r="10"/></svg>
    <span>Cyber Security</span></div>
  <div class="service" style="top:290px">
    <svg viewBox="0 0 62 58" fill="none" stroke="#fff" stroke-width="2"><path d="M18 2 L26 10 H36 L44 2 L54 10 V56 H8 V10 Z M31 10 V56 M8 30 H54 M8 42 H54"/></svg>
    <span>Risk Management</span></div>
  <div class="service" style="top:370px">
    <svg viewBox="0 0 62 58" fill="none" stroke="#fff" stroke-width="2"><rect x="21" y="2" width="20" height="16"/><path d="M31 18 V28 M9 28 H53 M9 28 V36 M31 28 V36 M53 28 V36"/><rect x="2" y="36" width="15" height="18"/><rect x="24" y="36" width="15" height="18"/><rect x="46" y="36" width="14" height="18"/></svg>
    <span>Project Management</span></div>
  <div class="service" style="top:450px">
    <svg viewBox="0 0 62 58" fill="none" stroke="#fff" stroke-width="2"><rect x="4" y="8" width="34" height="36"/><path d="M10 38 V30 M16 38 V24 M22 38 V28 M30 16 L40 10 L48 14 L58 4"/><circle cx="44" cy="42" r="12"/><circle cx="44" cy="42" r="5"/></svg>
    <span>Data Analytics Consulting</span></div>
</section>

<!-- discs around news -->
<div class="disc" style="left:945px;top:1423px;width:242px;height:242px;clip-path:inset(123px 0 0 0)"></div>
<div class="disc light" style="left:899px;top:1546px;width:72px;height:72px"></div>

<!-- news -->
<h2 class="heading" style="top:1616px">News and Events</h2>
<article class="card" style="left:144px">
  <div class="card-img" role="img" aria-label="Technician with laptop in a server aisle lit in teal" style="background:linear-gradient(135deg,#0e2a33,#1d6670,#0c1e28)"></div>
  <h3 class="card-title">Pellentesque convallis molestie enim sit amet efficitur</h3>
  <p class="card-date">22 December, 2020</p>
</article>
<article class="card" style="left:456px">
  <div class="card-img" role="img" aria-label="Developers pointing at code on desktop monitors" style="background:linear-gradient(135deg,#6e5a4e,#2b3a45,#d9d9d6)"></div>
  <h3 class="card-title">Vivamus lacus justo, ultrices nec erat in, euismod iaculis mauris</h3>
  <p class="card-date">22 December, 2020</p>
</article>
<article class="card" style="left:768px">
  <div class="card-img" role="img" aria-label="Digital globe made of glowing network points on dark blue" style="background:linear-gradient(135deg,#071630,#123b5c,#081a33)"></div>
  <h3 class="card-title">Fusce vitae lectus sit amet mi pulvinar maximus placerat eget</h3>
  <p class="card-date">22 December, 2020</p>
</article>
<div class="btn-solid" style="left:544px;top:1963px">View All</div>

<!-- disc above experts -->
<div class="disc" style="left:-24px;top:2059px;width:308px;height:308px"></div>
<div class="disc light" style="left:29px;top:2023px;width:72px;height:72px"></div>

<!-- experts -->
<div class="abs experts-band"></div>
<h2 class="heading" style="top:2167px">Our Experts</h2>
<svg class="arrow" style="left:50px;top:2324px" width="18" height="28" viewBox="0 0 18 28"><path d="M14 3 L4 14 L14 25" fill="none" stroke="#333" stroke-width="3.5"/></svg>
<svg class="arrow" style="left:1131px;top:2324px" width="18" height="28" viewBox="0 0 18 28"><path d="M4 3 L14 14 L4 25" fill="none" stroke="#333" stroke-width="3.5"/></svg>
<div class="expert" style="left:144px">
  <div class="expert-photo" role="img" aria-label="Portrait photo of expert Daniel Reeve"></div>
  <div class="expert-name">Daniel Reeve</div>
  <div class="expert-role">Proin eget congue</div>
  <div class="expert-rule"></div>
  <p class="expert-bio">Maecenas vel tortor accumsan quam varius imperdiet vel eget elit. Aenean facilisis tincidunt lectus, id dictum nisi luctus eget. Vivamus efficitur ex condimentum</p>
  <div class="expert-more">Read More</div>
</div>
<div class="expert" style="left:621px">
  <div class="expert-photo" role="img" aria-label="Portrait photo of expert Clara"></div>
  <div class="expert-name">Clara</div>
  <div class="expert-role">Proin eget congue</div>
  <div class="expert-rule"></div>
  <p class="expert-bio">Maecenas vel tortor accumsan quam varius imperdiet vel eget elit. Aenean facilisis tincidunt lectus, id dictum nisi luctus eget. Vivamus efficitur ex condimentum</p>
  <div class="expert-more">Read More</div>
</div>

<!-- contact -->
<h2 class="heading" style="top:2599px">Contact Us</h2>
<div class="field" style="left:144px;top:2652px;width:218px;height:40px">Name</div>
<div class="field" style="left:375px;top:2652px;width:218px;height:40px">Email</div>
<div class="field" style="left:607px;top:2652px;width:217px;height:40px">Phone</div>
<div class="field" style="left:837px;top:2652px;width:218px;height:40px">Title</div>
<div class="field" style="left:144px;top:2707px;width:911px;height:112px">Message</div>
<div class="btn-solid" style="left:544px;top:2837px">Submit</div>

<div class="disc" style="left:916px;top:2892px;width:266px;height:266px"></div>
<div class="disc light" style="left:1097px;top:2876px;width:72px;height:72px"></div>

<!-- footer -->
<footer class="abs footer">
  <div class="abs footer-links">Home &nbsp;| &nbsp;About Harwell &nbsp;| &nbsp;Our Experts &nbsp;| &nbsp;News and Events &nbsp;| &nbsp;Careers &nbsp;| &nbsp;Contact Us</div>
  <div class="abs footer-copy">Copyright &copy; 2020 &nbsp;Harwell Mariner Advisory LLC. &nbsp; All rights reserved.</div>
  <div class="social" style="left:990px" aria-label="Social profile"></div>
  <div class="social" style="left:1034px" aria-label="Social profile"></div>
</footer>

</body>
</html>
```